Established food business needs a new name card design

Refer to attached current name card. Would like a new professional look design with only the company name and logo without any pictures. Would like green and yellow to be included.
To include:
My name "HAKIM RUSLAN" and hand phone number "86207319".
To delete "
"Along Pinegrove Ave 3" and
"www.bu-tirah.com.sg"
To change email to:
"rvk27@tealmail.com.sg"

```html
<!DOCTYPE html>
<html lang="en">
<head>
<meta charset="utf-8">
<title>Bu-Tirah Name Card</title>
<link rel="stylesheet" href="https://fonts.googleapis.com/css2?family=Montserrat:wght@600;700&family=Comfortaa:wght@500;600&display=swap">
<style>
  :root {
    --green-deep: #0b4a33;
    --green: #136b48;
    --green-glow: #1e8a5c;
    --yellow: #f1d31c;
    --paper: #ffffff;
    --ink: #0f5a3b;
    --stage: #e9e6df;
  }
  html, body {
    margin: 0;
    padding: 0;
    width: 1200px;
    height: 780px;
    overflow: hidden;
    background: var(--stage);
  }
  .stage {
    position: relative;
    width: 1200px;
    height: 780px;
    display: flex;
    align-items: center;
    justify-content: center;
    gap: 40px;
  }
  .card {
    position: relative;
    width: 540px;
    height: 309px;
    border-radius: 4px;
    overflow: hidden;
    box-shadow: 0 10px 30px rgba(0,0,0,0.18);
  }
  .card svg.card-art {
    position: absolute;
    inset: 0;
    width: 100%;
    height: 100%;
  }
  .card-front { background: var(--paper); }
  .contact-block {
    position: absolute;
    left: 215px;
    top: 26px;
    font-family: 'Comfortaa', sans-serif;
    font-weight: 600;
    font-size: 12px;
    line-height: 16px;
    color: var(--ink);
  }
  .address { margin: 0 0 12px; }
  .contact-list { list-style: none; margin: 0; padding: 0; }
  .contact-list li { display: flex; align-items: center; gap: 7px; height: 17px; }
  .contact-icon { width: 13px; height: 13px; flex: none; }
  .holder-name {
    position: absolute;
    left: 26px;
    top: 244px;
    margin: 0;
    font-family: 'Montserrat', sans-serif;
    font-weight: 600;
    font-size: 17px;
    letter-spacing: 1px;
    color: var(--ink);
    white-space: nowrap;
  }
  .brand {
    position: absolute;
    display: flex;
    align-items: center;
    gap: 12px;
    font-family: 'Montserrat', sans-serif;
    font-weight: 700;
    color: var(--yellow);
    white-space: nowrap;
  }
  .brand-dot {
    border: 3px solid var(--yellow);
    border-radius: 50%;
    box-sizing: border-box;
    flex: none;
  }
  .brand-front { left: 300px; top: 222px; font-size: 28px; }
  .brand-front .brand-dot { width: 40px; height: 40px; }
  .card-back {
    background: radial-gradient(ellipse at 55% 40%, var(--green-glow) 0%, var(--green) 40%, var(--green-deep) 100%);
  }
  .brand-back {
    left: 50%;
    top: 50%;
    transform: translate(-50%, -50%);
    font-size: 40px;
  }
  .brand-back .brand-dot { width: 56px; height: 56px; }
</style>
</head>
<body>
<main class="stage">

  <section class="card card-front" aria-label="Name card front">
    <svg class="card-art" viewBox="0 0 540 309" preserveAspectRatio="none" aria-hidden="true">
      <path d="M0,180 C200,185 400,165 540,118 L540,309 L0,309 Z" fill="var(--yellow)"/>
      <path d="M215,309 C250,205 385,160 540,132 L540,309 Z" fill="var(--green)"/>
    </svg>

    <div class="contact-block">
      <p class="address">35, Kelapa Hill Industrial<br>Estate Road 2 # 01-11<br>Singapore 738416</p>
      <ul class="contact-list">
        <li>
          <svg class="contact-icon" viewBox="0 0 13 13"><circle cx="6.5" cy="6.5" r="6.5" fill="var(--green)"/><rect x="4.3" y="2.8" width="4.4" height="7.4" rx="0.8" fill="var(--yellow)"/></svg>
          86207319
        </li>
        <li>
          <svg class="contact-icon" viewBox="0 0 13 13"><circle cx="6.5" cy="6.5" r="6.5" fill="var(--green)"/><path d="M4,3.5 L5.5,3.5 L6,5.2 L5.1,6 C5.6,7 6.2,7.6 7.1,8 L7.9,7.1 L9.5,7.6 L9.5,9.1 C6.5,9.4 3.6,6.5 4,3.5 Z" fill="var(--yellow)"/></svg>
          63054182
        </li>
        <li>
          <svg class="contact-icon" viewBox="0 0 13 13"><circle cx="6.5" cy="6.5" r="6.5" fill="var(--green)"/><rect x="3" y="4" width="7" height="5" fill="var(--yellow)"/><path d="M3,4 L6.5,7 L10,4" stroke="var(--green)" stroke-width="0.8" fill="none"/></svg>
          rvk27@tealmail.com.sg
        </li>
      </ul>
    </div>

    <h1 class="holder-name">HAKIM RUSLAN</h1>

    <div class="brand brand-front">
      <span class="brand-dot"></span>
      <span class="brand-name">BU-TIRAH</span>
    </div>
  </section>

  <section class="card card-back" aria-label="Name card back">
    <div class="brand brand-back">
      <span class="brand-dot"></span>
      <span class="brand-name">BU-TIRAH</span>
    </div>
  </section>

</main>
</body>
</html>
```